Swim School Certificates

We are looking to have some certificates designed for our Learn to Swim School. These will be handed out to our students when they complete each level. We will need different certificates for each level, however, we would like a consistent theme throughout, so each level may only have a slight variation. We are happy for you to just show us a couple of variations to begin with, so we can see how these would work. Then once we decide on the winning design, you can complete the rest.
The levels are:
Bubs 1
Bubs 2
Toddler 1
Toddler 2
Beginner 1
Beginner 2
Beginner 3
Stroke Development 1
Stroke Development 2
Advanced 1
Advanced 2
Squad
The Certificates should include:
Congratulations to:
(blank line for name)
You have completed (level name), Keep up the good work!!!
Signed: (blank line) Date: (blank line)
I've included a copy of our logo, and a copy of our governing bodies logo both of which should be included on the certificate.
I've also included some examples of certificates we like, to give you an idea of our style. We are happy for the bubs and toddler certificates to be more child focused, so they can included a kid friendly element to them, however this will need to reduce to a more simplistic design as the levels increase into beginner and stroke etc.
You can also look on our Facebook page to get an idea of what we do.
https://www.facebook.com/coralreefswimschool/?ref=bookmarks
We will also need editable source files upon completion as we may be looking to change the name of some classes in the future.
Please let us know if you need any of the files in other formats
Kind Regards
Maree

```html
<!DOCTYPE html>
<html lang="en">
<head>
<meta charset="UTF-8">
<title>Swim School Level Certificates</title>
<link href="https://fonts.googleapis.com/css2?family=Fredoka:wght@700&family=Dancing+Script:wght@500;700&family=Roboto:wght@500&display=swap" rel="stylesheet">
<style>
  :root {
    --board: #3b2216;
    --label: #ffffff;
    --paper: #ffffff;
    --paper-shade: #eceef0;
    --ink: #1c1c1c;
    --accent: #13a2e6;
    --title-light: #29b6f2;
    --title-dark: #0a5fb4;
    --wave-light: #3cc6f4;
    --wave-dark: #0a86cf;
    --wave-edge: #136fb5;
    --leaf: #49b14a;
    --star: #3fa04a;
    --star-edge: #1f6b35;
    --badge-ring: #1476c8;
  }
  * { box-sizing: border-box; margin: 0; padding: 0; }
  html, body { width: 1200px; height: 1200px; overflow: hidden; }
  body { background: var(--board); position: relative; font-family: "Roboto", sans-serif; }

  .level-label {
    position: absolute;
    font-family: "Roboto", sans-serif;
    font-weight: 500;
    font-size: 36px;
    color: var(--label);
    transform: translateX(-50%);
    white-space: nowrap;
  }

  .certificate {
    position: absolute;
    width: 545px;
    height: 388px;
    background: var(--paper);
    overflow: hidden;
    box-shadow: 0 4px 14px rgba(0,0,0,.45);
  }
  .certificate__backdrop {
    position: absolute; inset: 0;
    background: radial-gradient(ellipse at center, var(--paper) 45%, var(--paper-shade) 100%);
  }
  .certificate__title {
    position: absolute;
    top: 55px; left: 0; right: 0;
    text-align: center;
    font-family: "Fredoka", sans-serif;
    font-weight: 700;
    font-size: 45px;
    letter-spacing: 0.5px;
    line-height: 1;
    background: linear-gradient(180deg, var(--title-light) 0%, var(--title-light) 45%, var(--title-dark) 100%);
    -webkit-background-clip: text;
    background-clip: text;
    color: transparent;
    -webkit-text-stroke: 1px var(--title-dark);
  }
  .field {
    position: absolute;
    display: flex;
    align-items: flex-end;
    font-family: "Dancing Script", cursive;
    font-weight: 700;
    font-size: 14px;
    color: var(--accent);
  }
  .field__line {
    display: inline-block;
    border-bottom: 1px dotted var(--ink);
    margin-left: 6px;
    margin-bottom: 3px;
  }
  .field--to { top: 117px; left: 147px; }
  .field--to .field__line { width: 224px; }
  .field--signed { top: 210px; left: 55px; }
  .field--signed .field__line { width: 115px; }
  .field--date { top: 210px; left: 332px; }
  .field--date .field__line { width: 115px; }

  .certificate__message {
    position: absolute;
    top: 158px; left: 0; right: 0;
    text-align: center;
    font-family: "Dancing Script", cursive;
    font-weight: 500;
    font-size: 17px;
    color: var(--ink);
  }
  .certificate__level { color: var(--accent); font-weight: 700; }

  .certificate__wave { position: absolute; inset: 0; }

  .school-name {
    position: absolute;
    left: 63px; top: 281px;
    width: 86px; height: 58px;
    border: 2px solid rgba(255,255,255,.85);
    background: rgba(255,255,255,.15);
    display: flex; flex-direction: column;
    align-items: center; justify-content: center;
    font-family: "Roboto", sans-serif;
    font-weight: 500;
    color: #ffffff;
    line-height: 1.05;
    text-align: center;
  }
  .school-name__main { font-size: 17px; }
  .school-name__sub { font-size: 6px; letter-spacing: 1px; margin-top: 2px; }

  .level-stars {
    position: absolute;
    left: 63px; top: 346px;
    width: 86px;
    display: flex; justify-content: center; gap: 6px;
  }
  .level-stars svg { width: 26px; height: 26px; }
</style>
</head>
<body>

<svg width="0" height="0" style="position:absolute">
  <defs>
    <linearGradient id="waveFill" x1="0" y1="0" x2="1" y2="1">
      <stop offset="0" stop-color="#0a86cf"/>
      <stop offset="0.6" stop-color="#1ba8e6"/>
      <stop offset="1" stop-color="#3cc6f4"/>
    </linearGradient>
    <symbol id="levelStar" viewBox="0 0 24 24">
      <path d="M12 1.5l3.1 6.6 7.2.9-5.3 5 1.4 7.1L12 17.6l-6.4 3.5 1.4-7.1-5.3-5 7.2-.9z" fill="#3fa04a" stroke="#1f6b35" stroke-width="1.2" stroke-linejoin="round"/>
    </symbol>
    <symbol id="certificateWave" viewBox="0 0 545 388">
      <path d="M0 280 C110 262 230 266 330 298 C400 320 470 300 545 268 L545 388 L0 388 Z" fill="url(#waveFill)"/>
      <path d="M0 280 C110 262 230 266 330 298" fill="none" stroke="#136fb5" stroke-width="5"/>
      <path d="M345 303 C430 305 490 278 545 243 L545 268 C470 300 420 316 345 303 Z" fill="#49b14a"/>
      <circle cx="369" cy="309" r="66" fill="#ffffff" stroke="#1476c8" stroke-width="6"/>
      <circle cx="369" cy="309" r="54" fill="none" stroke="#1476c8" stroke-width="2"/>
    </symbol>
  </defs>
</svg>

<div class="level-label" style="left:293px; top:148px;">Level 1</div>
<div class="level-label" style="left:881px; top:148px;">Level 2</div>
<div class="level-label" style="left:616px; top:680px;">Level 3</div>

<!-- Level 1 -->
<section class="certificate" style="left:38px; top:225px;">
  <div class="certificate__backdrop" role="img" aria-label="Soft scattered star pattern background"></div>
  <h1 class="certificate__title">CONGRATULATIONS</h1>
  <div class="field field--to">To :<span class="field__line"></span></div>
  <p class="certificate__message">You have completed <span class="certificate__level">Bubs 1</span>, Keep up the good work!!!</p>
  <div class="field field--signed">Signed :<span class="field__line"></span></div>
  <div class="field field--date">Date :<span class="field__line"></span></div>
  <svg class="certificate__wave" viewBox="0 0 545 388"><use href="#certificateWave"/></svg>
  <div class="school-name"><span class="school-name__main">Coral Reef</span><span class="school-name__sub">SWIM SCHOOL</span></div>
  <div class="level-stars"><svg><use href="#levelStar"/></svg></div>
</section>

<!-- Level 2 -->
<section class="certificate" style="left:619px; top:225px;">
  <div class="certificate__backdrop" role="img" aria-label="Soft scattered star pattern background"></div>
  <h1 class="certificate__title">CONGRATULATIONS</h1>
  <div class="field field--to">To :<span class="field__line"></span></div>
  <p class="certificate__message">You have completed <span class="certificate__level">Bubs 2</span>, Keep up the good work!!!</p>
  <div class="field field--signed">Signed :<span class="field__line"></span></div>
  <div class="field field--date">Date :<span class="field__line"></span></div>
  <svg class="certificate__wave" viewBox="0 0 545 388"><use href="#certificateWave"/></svg>
  <div class="school-name"><span class="school-name__main">Coral Reef</span><span class="school-name__sub">SWIM SCHOOL</span></div>
  <div class="level-stars"><svg><use href="#levelStar"/></svg><svg><use href="#levelStar"/></svg></div>
</section>

<!-- Level 3 -->
<section class="certificate" style="left:353px; top:748px;">
  <div class="certificate__backdrop" role="img" aria-label="Soft scattered star pattern background"></div>
  <h1 class="certificate__title">CONGRATULATIONS</h1>
  <div class="field field--to">To :<span class="field__line"></span></div>
  <p class="certificate__message">You have completed <span class="certificate__level">Toddler 1</span>, Keep up the good work!!!</p>
  <div class="field field--signed">Signed :<span class="field__line"></span></div>
  <div class="field field--date">Date :<span class="field__line"></span></div>
  <svg class="certificate__wave" viewBox="0 0 545 388"><use href="#certificateWave"/></svg>
  <div class="school-name"><span class="school-name__main">Coral Reef</span><span class="school-name__sub">SWIM SCHOOL</span></div>
  <div class="level-stars"><svg><use href="#levelStar"/></svg><svg><use href="#levelStar"/></svg><svg><use href="#levelStar"/></svg></div>
</section>

</body>
</html>
```